Small Creativity Consulting Business Needs Annual Report Design

I need interior e-print design for a 14-page digital annual report to go out to our consumers and audiences (@3000 people). I have a small creativity consulting business that provides consulting services, programs, keynotes, and products designed to helped creative people be more productive and productive people be more creative. The report should not feel corporate but instead should feel consistent with the brand - Gathering Lantern - like a well-crafted field guide. Colors should be consistent with the burnt orange, deep red, and green used in our existing branding.
Burnt red color: 691419
Orange color: CF7019
Green color: 64600D

The final design should convey wonder mixed with wisdom and sound entrepreneurial guidance.

Target Market(s)

women & men, 30s-60s, who love creativity, the arts, books + who want to create & produce

Industry/Entity Type

Digital

Requirements
Must have
• The report should not feel corporate but instead should feel consistent with the brand - Gathering Lantern - like a well-crafted field guide. Colors should be consistent with the burnt orange, deep red, and green used in our existing branding.
Burnt red color: 691419
Orange color: CF7019
Green color: 64600D

It should include many of the photos we have attached.

Nice to have
• You might play on the Harwick Viaduct image toward the end.
Should not have
• Don't aim for "cute" or "jazzy" creative. We're a more subdued creativity brand - although "bold" is good.

```html
<!DOCTYPE html>
<html lang="en">
<head>
<meta charset="utf-8">
<title>Gathering Lantern — Lantern Notes, page 2</title>
<link href="https://fonts.googleapis.com/css2?family=Cormorant+SC:wght@500;600&family=Libre+Baskerville:ital@0;1&family=Baskervville&display=swap" rel="stylesheet">
<style>
  :root {
    --backdrop: #ffffff;
    --paper: #ffffff;
    --ink: #1c1a18;
    --orange: #cf7019;
    --burnt-red: #691419;
    --green: #64600d;
    --quote-ink: #f7f3ee;
  }
  * { margin: 0; padding: 0; box-sizing: border-box; }
  html, body {
    width: 1200px; height: 1000px; overflow: hidden;
    background: var(--backdrop);
  }
  .page {
    position: absolute; left: 302px; top: 79px;
    width: 595px; height: 842px;
    background: var(--paper);
  }
  .hero {
    position: absolute; left: 0; top: 0; width: 595px; height: 337px;
    background:
      radial-gradient(ellipse 120px 160px at 30px 200px, rgba(200,60,120,.55), transparent 70%),
      radial-gradient(ellipse 110px 150px at 210px 250px, rgba(140,110,200,.55), transparent 70%),
      radial-gradient(ellipse 120px 140px at 420px 160px, rgba(170,200,150,.5), transparent 70%),
      linear-gradient(90deg, #5e1a34 0%, #8a3a66 14%, #6a4f8a 32%, #2f6a66 50%, #3f6a3a 66%, #6e6a4a 80%, #6a2e22 100%);
  }
  .hero-question {
    position: absolute; left: 77px; top: 46px;
    font-family: "Libre Baskerville", Georgia, serif;
    font-style: italic; font-size: 15px; line-height: 23px;
    color: var(--quote-ink);
  }
  .section-title {
    position: absolute; left: 76px; top: 376px;
    font-family: "Cormorant SC", Georgia, serif;
    font-weight: 600; font-size: 33px; line-height: 1;
    color: var(--orange); letter-spacing: 0;
  }
  .body-copy {
    position: absolute; left: 77px; top: 425px; width: 448px;
    font-family: "Baskervville", "Libre Baskerville", Georgia, serif;
    font-size: 11px; line-height: 14.6px; color: var(--ink);
    font-variant-numeric: lining-nums;
  }
  .body-copy p { margin-bottom: 14.6px; }
  .body-copy p.tight { margin-bottom: 0; }
  .brand-mark {
    position: absolute; left: 0; width: 595px; top: 774px;
    display: flex; flex-direction: column; align-items: center; gap: 5px;
  }
  .brand-name {
    font-family: "Baskervville", Georgia, serif;
    font-size: 11px; color: var(--ink);
  }
  .brand-dot { width: 6px; height: 6px; border-radius: 50%; background: var(--ink); }
  .folio {
    position: absolute; left: 553px; top: 800px;
    font-family: "Baskervville", Georgia, serif; font-size: 10px; color: var(--ink);
    font-variant-numeric: lining-nums;
  }
</style>
</head>
<body>
  <article class="page">
    <div class="hero" role="img" aria-label="Close-up photograph of a translucent leaf skeleton washed in magenta, violet, teal and green light">
      <p class="hero-question">Where are you in work, creating,<br>and relationship<br>that you weren’t five years ago<br>that you’re grateful for?</p>
    </div>

    <h1 class="section-title">You Are Here</h1>

    <div class="body-copy">
      <p>In 2012, I’m in the middle but I’m neither stuck nor lost. I’m in the middle of my life. My little girl turned three this July two days before my father died and three days before he would have turned 74. Some days, my body seems like a fragile mobile home vulnerable to unpredictable winds. Other days, it astounds me with its capacity for renewal and agency of this creative mind. My father’s absence, my daughter’s presence, and my wife’s partnership remind me daily of how extraordinary the simplest things are.</p>
      <p>Every day holds so much promise.</p>
      <p class="tight">I’m in the middle of my next book. The singular elegant idea conceived, the structure designed, the research near-complete, the next leg of intense work begins. The book looks nothing like its original conception a few years ago.</p>
      <p>I’m in the middle of my business. It’s assumed different shapes the past few years, but its latest incarnation took clear shape this year.</p>
      <p>When you’re in the middle - of your life, your business, your book - wonder is a welcome ally. Wonder rattles your perspective on what matters and what your life and work mean to yourself, your loved ones, your audience and customers.</p>
      <p>This dispatch, LANTERN NOTES, is an opportunity for me to reflect on what has happened this year, give you a peak behind the scenes of Gathering Lantern, and share with you some take-aways that might prompt your own LANTERN NOTES.</p>
    </div>

    <div class="brand-mark">
      <span class="brand-name">Gathering Lantern</span>
      <span class="brand-dot"></span>
    </div>
    <span class="folio">2</span>
  </article>
</body>
</html>
```